Potato chips bag design of 85 gram for Greek and East Europe market

I want a new design for a new potato chips bag for the Greek market. The product is going to be all natural ingredient, gluten free, preservatives free, allergen free from Greek organic potatoes . Thick cut, marinated potatoes that are premium vs others. For packaging we want it to stand out on shelf. Have a Matt film . It will be called Silverbrook Tumble. Salt and Oregano flavors to start with.
Ideally to stand out on shelf we were thinking to have a black/white Color pallet and have an artistic pattern printed like the pictures attached. But of course open to ideas.
Target Market(s)
Greece and East Europe
Industry/Entity Type
Snacks Packaged goods
Requirements
Must have
- Matt film that stands out on shelf . 85 grams bag so 25cm tall and 15 cms length
Nice to have
- Ideally black/white pallet as it looks more premium. Patterns artistic that will make it look like art.
Should not have
- Traditional Pevo type of design (red-green colors etc)

```html
<!DOCTYPE html>
<html lang="en">
<head>
<meta charset="utf-8">
<title>Silverbrook Tumble Potato Chips – Bag Fronts</title>
<link rel="stylesheet" href="https://fonts.googleapis.com/css2?family=Amatic+SC:wght@700&family=Oswald:wght@400;500&display=swap">
<style>
  :root {
    --bg: #e9e9ea;
    --bag: #f7f7f6;
    --ink: #4a4a50;
    --ink-soft: #8b8d92;
    --oregano: #8f9a3e;
    --salt: #23b6d8;
    --badge: #3fb24f;
    --chip-light: #f6e3a0;
    --chip-mid: #e9b955;
    --chip-deep: #d2763a;
    --wave-dark: #5e5f63;
    --wave-light: #c9cacc;
    --seal: #e2e2e1;
  }
  * { box-sizing: border-box; margin: 0; padding: 0; }
  html, body { width: 1200px; height: 900px; overflow: hidden; }
  body {
    background: var(--bg);
    display: flex; align-items: center; justify-content: center; gap: 70px;
  }
  .bag {
    position: relative; width: 420px; height: 720px;
    background: var(--bag);
    display: flex; flex-direction: column; align-items: center;
    box-shadow: 0 10px 30px rgba(0,0,0,.12);
    overflow: hidden;
  }
  .bag--oregano { --accent: var(--oregano); }
  .bag--salt { --accent: var(--salt); }
  .seal {
    width: 100%; height: 26px; background: var(--seal);
    background-image: repeating-linear-gradient(180deg, transparent 0 3px, rgba(0,0,0,.06) 3px 4px);
    flex: none;
  }
  .brand {
    margin-top: 26px; text-align: center;
    font-family: 'Amatic SC', cursive; font-weight: 700;
    color: var(--ink); font-size: 76px; line-height: .82; letter-spacing: 4px;
  }
  .subbrand {
    display: flex; align-items: center; gap: 10px; margin-top: 6px;
    font-family: 'Amatic SC', cursive; font-weight: 700;
    color: var(--accent); font-size: 44px; letter-spacing: 6px; line-height: 1;
  }
  .subbrand::before, .subbrand::after {
    content: ""; width: 50px; height: 2px; background: var(--accent);
  }
  .product-row { display: flex; align-items: center; gap: 10px; margin-top: 2px; }
  .organic-badge {
    width: 62px; height: 62px; border-radius: 50%;
    border: 4px solid var(--badge); flex: none;
  }
  .product {
    font-family: 'Oswald', sans-serif; font-weight: 500;
    color: var(--ink); font-size: 48px; line-height: 1;
  }
  .tagline {
    margin-top: 10px; text-align: center;
    font-family: 'Oswald', sans-serif; font-weight: 500;
    color: var(--ink); font-size: 19px; line-height: 1.1; letter-spacing: 1px;
  }
  .chips-photo {
    position: relative; width: 100%; height: 170px; margin-top: 12px;
    background: radial-gradient(ellipse at 40% 40%, var(--chip-light) 0%, var(--chip-mid) 55%, var(--chip-deep) 100%);
    display: flex; align-items: center; justify-content: center;
  }
  .flavor {
    font-family: 'Amatic SC', cursive; font-weight: 700;
    color: var(--accent); font-size: 62px; letter-spacing: 2px;
    transform: rotate(8deg);
  }
  .key-band { width: 100%; height: 26px; background: var(--ink-soft); flex: none; }
  .waves {
    position: relative; width: 100%; flex: 1;
    background: linear-gradient(180deg, var(--wave-dark), var(--wave-light) 50%, var(--wave-dark));
  }
  .claims {
    position: absolute; left: 50%; bottom: 34px; transform: translateX(-50%);
    display: flex; align-items: center; gap: 14px;
  }
  .claim-badge { background: var(--badge); border-radius: 6px; }
  .claim-badge--wide { width: 92px; height: 36px; }
  .claim-badge--square { width: 42px; height: 42px; }
  .net-weight {
    font-family: 'Oswald', sans-serif; font-weight: 500; color: var(--badge);
    text-align: center; line-height: 1; background: var(--bag); padding: 3px 5px; border-radius: 4px;
  }
  .net-weight .label { font-size: 11px; display: block; }
  .net-weight .value { font-size: 26px; display: block; }
  .net-weight .unit { font-size: 9px; display: block; }
</style>
</head>
<body>
  <article class="bag bag--oregano">
    <div class="seal"></div>
    <h1 class="brand">SILVER<br>BROOK</h1>
    <p class="subbrand">TUMBLE</p>
    <div class="product-row">
      <span class="organic-badge"></span>
      <h2 class="product">POTATO CHIPS</h2>
    </div>
    <p class="tagline">MADE FROM PREMIUM GREEK<br>ORGANIC MARINATED POTATOES</p>
    <div class="chips-photo" role="img" aria-label="Photograph of ridged golden potato chips">
      <p class="flavor">ORIGINAL OREGANO</p>
    </div>
    <div class="key-band" role="img" aria-label="Greek key meander border"></div>
    <div class="waves" role="img" aria-label="Hand-drawn black and white swirling wave pattern">
      <div class="claims">
        <span class="claim-badge claim-badge--wide"></span>
        <span class="claim-badge claim-badge--square"></span>
        <p class="net-weight"><span class="label">NET.WT</span><span class="value">85</span><span class="unit">GRAMS</span></p>
      </div>
    </div>
    <div class="seal"></div>
  </article>

  <article class="bag bag--salt">
    <div class="seal"></div>
    <h1 class="brand">SILVER<br>BROOK</h1>
    <p class="subbrand">TUMBLE</p>
    <div class="product-row">
      <span class="organic-badge"></span>
      <h2 class="product">POTATO CHIPS</h2>
    </div>
    <p class="tagline">MADE FROM PREMIUM GREEK<br>ORGANIC MARINATED POTATOES</p>
    <div class="chips-photo" role="img" aria-label="Photograph of ridged golden potato chips">
      <p class="flavor">PERFECTLY SALTED</p>
    </div>
    <div class="key-band" role="img" aria-label="Greek key meander border"></div>
    <div class="waves" role="img" aria-label="Hand-drawn black and white swirling wave pattern">
      <div class="claims">
        <span class="claim-badge claim-badge--wide"></span>
        <span class="claim-badge claim-badge--square"></span>
        <p class="net-weight"><span class="label">NET.WT</span><span class="value">85</span><span class="unit">GRAMS</span></p>
      </div>
    </div>
    <div class="seal"></div>
  </article>
</body>
</html>
```